window design for Pellworth's Butcher Shop

Design an attractive window design (decals) for an old storefront (copy uploaded), which must be very inviting and eye-catching. The old awning (K & T Meats) is being removed and replaced with Pellworth's Butcher Shop (see copy of proposed awning uploaded)

I was inspired by another window decal design (copy uploaded) from Europe. I liked the use of the grey border on the lowest portion of the windows with the lettering in white. I thought the lettering was very eye-catching.

I also liked the use of reds, greys, blacks and whites to match our logo.

I liked the red ribbons incorporated into the grey lower portion of the windows, as well.

There will be a hanging industrial RED dome light installed in each window left and right sides.

WORDING FOR CENTER OF left WINDOW:
-Dry Aged Beef
-Homemade Sausage
WORDING FOR CENTER OF right WINDOW:
-Farm Fresh Poultry
-Wild Game
WORDING FOR LOWEST PORTION OF (left) WINDOW:
-Deli
-Catering
WORDING FOR LOWEST PORTION OF (RIGHT) WINDOW:
-Homestyle Cooking
-Fresh Pasta

The design should not block the view of the inside of the store. I would still like the street traffic to see inside the store (cope uploaded)

Target Market(s)

Middle Income, Italian and Hispanic Clientele

Industry/Entity Type

Shop

Colors
ec1f27
333333
fbfbfb

Requirements
Must have
• use of reds, greys and whites
Nice to have
• I have uploaded a photo from Europe that inspired me
• A more sophisticated design
Should not have
• -Should not block the view into the store
• -Animals are not a must in the design. Ex: cow, pig, chicken, etc.

```html
<!DOCTYPE html>
<html lang="en">
<head>
<meta charset="utf-8">
<title>Pellworth's Storefront Window Decals</title>
<link rel="stylesheet" href="https://fonts.googleapis.com/css2?family=Lobster&display=swap">
<style>
  :root{
    --red:#ec1f27;
    --charcoal:#333333;
    --ink:#111111;
    --white:#fbfbfb;
    --paper:#eeeeee;
    --script:'Lobster', cursive;
  }
  *{margin:0;padding:0;box-sizing:border-box}
  html,body{width:1200px;height:670px;overflow:hidden;background:var(--paper)}
  .canvas{position:relative;width:1200px;height:670px;overflow:hidden;background:var(--paper);font-family:var(--script)}

  .project-title{position:absolute;left:35px;top:18px;color:var(--charcoal);font-size:24px;line-height:29px;font-weight:400}

  .band{position:absolute;left:0;width:1200px}
  .band--red{top:89px;height:49px;background:var(--red)}
  .band--dark{top:138px;height:25px;background:var(--charcoal)}
  .band--pinstripe{top:163px;height:3px;background:var(--red)}
  .band--white{top:166px;height:6px;background:var(--white)}
  .band--base{top:172px;height:14px;background:var(--charcoal)}

  .interior{position:absolute;left:0;top:186px;width:1200px;height:406px;
    background:linear-gradient(100deg,#c96a66 0%,#dcb2ac 22%,#d8cfcc 45%,#cfc8c4 60%,#e2dcd8 80%,#ede9e4 100%)}

  .kickplate{position:absolute;top:490px;height:102px;background:var(--charcoal)}
  .kickplate--left{left:0;width:543px}
  .kickplate--right{left:725px;width:475px}

  .mullion{position:absolute;top:186px;width:3px;height:406px;background:var(--ink)}
  .mullion--edge-left{left:0}
  .mullion--a{left:364px}
  .mullion--b{left:542px}
  .mullion--c{left:724px}
  .mullion--d{left:913px}
  .mullion--edge-right{left:1197px}
  .door{position:absolute;left:566px;top:244px;width:136px;height:346px;border:3px solid var(--ink);border-bottom:none}

  .seal{position:absolute;border-radius:50%;background:var(--ink);display:flex;align-items:center;justify-content:center}
  .seal--awning{left:566px;top:70px;width:136px;height:136px;border:4px solid var(--white);box-shadow:inset 0 0 0 9px var(--ink),inset 0 0 0 12px var(--red)}
  .seal--door{left:596px;top:318px;width:76px;height:76px;border:2px solid var(--white);box-shadow:inset 0 0 0 4px var(--ink),inset 0 0 0 6px var(--red)}
  .seal-name{color:var(--white);font-family:var(--script);font-weight:400}
  .seal--awning .seal-name{font-size:20px}
  .seal--door .seal-name{font-size:12px}

  .decal-art{position:absolute;background:var(--red);border-radius:40%}
  .decal-art--cow{left:236px;top:294px;width:80px;height:44px}
  .decal-art--links{left:80px;top:358px;width:78px;height:46px;border-radius:50%}
  .decal-art--hen{left:922px;top:234px;width:62px;height:48px}
  .decal-art--stag{left:1114px;top:328px;width:66px;height:78px}

  .decal-word{position:absolute;color:var(--red);font-family:var(--script);font-weight:400;white-space:nowrap;line-height:1.2;
    -webkit-text-stroke:7px var(--white);paint-order:stroke fill;transform-origin:center}
  .decal-word--beef{left:61px;top:262px;font-size:44px;transform:rotate(-20deg)}
  .decal-word--sausage{left:36px;top:389px;font-size:42px;transform:rotate(-20deg)}
  .decal-word--poultry{left:912px;top:278px;font-size:34px;transform:rotate(-16deg)}
  .decal-word--game{left:925px;top:368px;font-size:40px;transform:rotate(-16deg)}

  .services{position:absolute;top:506px;list-style:none;color:var(--white);font-size:24px;line-height:29px}
  .services li::before{content:"\2022";margin-right:6px}
  .services--left{left:90px}
  .services--right{left:934px}
</style>
</head>
<body>
<main class="canvas">
  <h1 class="project-title">Pellworth's Storefront<br>48-12 Linden Ave</h1>

  <div class="band band--red"></div>
  <div class="band band--dark"></div>
  <div class="band band--pinstripe"></div>
  <div class="band band--white"></div>
  <div class="band band--base"></div>

  <div class="interior" role="img" aria-label="View through the windows into the butcher shop interior: meat display counters, hanging cuts and refrigerated cases"></div>

  <div class="kickplate kickplate--left"></div>
  <div class="kickplate kickplate--right"></div>

  <div class="mullion mullion--edge-left"></div>
  <div class="mullion mullion--a"></div>
  <div class="mullion mullion--b"></div>
  <div class="mullion mullion--c"></div>
  <div class="mullion mullion--d"></div>
  <div class="mullion mullion--edge-right"></div>
  <div class="door"></div>

  <div class="seal seal--awning"><span class="seal-name">Pellworth's</span></div>
  <div class="seal seal--door"><span class="seal-name">Pellworth's</span></div>

  <div class="decal-art decal-art--cow" role="img" aria-label="Red cow silhouette decal"></div>
  <div class="decal-art decal-art--links" role="img" aria-label="Red sausage links decal"></div>
  <div class="decal-art decal-art--hen" role="img" aria-label="Red hen silhouette decal"></div>
  <div class="decal-art decal-art--stag" role="img" aria-label="Red leaping stag silhouette decal"></div>

  <p class="decal-word decal-word--beef">Dry Aged Beef</p>
  <p class="decal-word decal-word--sausage">Homemade Sausage</p>
  <p class="decal-word decal-word--poultry">Fresh Farm Poultry</p>
  <p class="decal-word decal-word--game">Wild Game</p>

  <ul class="services services--left">
    <li>Deli</li>
    <li>Fresh Pasta</li>
  </ul>
  <ul class="services services--right">
    <li>Catering</li>
    <li>Homestyle Cooking</li>
  </ul>
</main>
</body>
</html>
```